Professional Business Card for Commercial Cleaning Company

We need a business card that represents our commercial janitorial cleaning company and represent several brands for our company so we do not want to highlight the logo too much. We want something that says we are professional.
Notes:No website or address as we have many locations and many websites and companies under our corporate name of "Brightvale Holdings, LLC" . Every time we hand a customer a business card they have contacted us via another brand we own but we don't want to have 21 business cards so we want to not focus on Brightvale Holdings, LLC too much since people will automatically ask "What is Brightvale Holdings, LLC" Example: Noodle Barn and Wrap Lantern restaurants are owned by "Zest! Brands" is the corporation name. Same principle here. Except we do not advertise at this time that all of our brands are connected. Hope this helps.
Target Market(s)
Commercial Cleaning
Industry/Entity Type
Janitorial Service
Contact Information for Business Card
Milo Jarvis
Business Development
555-382-9047
sales@brightvaleholdingsllc.example
Requirements
Must have
- Logo with contact information, need to be able to easily edit contact info for others in my office.
Nice to have
- Professional Image. Like to see a colorful bold look and a more standard business card look.
Should not have
- Any type of cleaning icons, tools, people or water.

```html
<!DOCTYPE html>
<html lang="en">
<head>
<meta charset="utf-8">
<title>Brightvale Holdings, LLC — Business Card</title>
<link rel="stylesheet" href="https://fonts.googleapis.com/css2?family=Lato:wght@400;700;900&display=swap">
<style>
  :root {
    --backdrop: #262626;
    --card-dark: #2f2f30;
    --card-light: #fdfdfd;
    --navy: #1f3a78;
    --green: #5fa83d;
    --ink: #2a2a2a;
  }
  * { margin: 0; padding: 0; box-sizing: border-box; }
  html, body {
    width: 1200px; height: 1200px; overflow: hidden;
    background: var(--backdrop);
    font-family: "Lato", sans-serif;
  }
  .sheet {
    width: 1200px; height: 1200px;
    display: flex; flex-direction: column; align-items: center; justify-content: center;
    gap: 52px;
  }
  .card {
    width: 900px; height: 514px;
    position: relative;
    overflow: hidden;
    box-shadow: 0 10px 30px rgba(0,0,0,0.35);
  }
  .card--front { background: var(--card-dark); }
  .card--back { background: var(--card-light); }

  .brand {
    position: absolute;
    display: flex; align-items: baseline; gap: 14px;
    white-space: nowrap;
  }
  .brand-name {
    font-family: "Lato", sans-serif;
    font-weight: 900;
    color: var(--navy);
    letter-spacing: -0.5px;
  }
  .brand-mark {
    width: 14px; height: 14px; flex: none;
    background: var(--green);
  }
  .card--front .brand {
    left: 0; right: 0; top: 50%;
    transform: translateY(-50%);
    justify-content: center;
  }
  .card--front .brand-name { font-size: 60px; }
  .card--back .brand { left: 60px; top: 70px; }
  .card--back .brand-name { font-size: 54px; }

  .holder {
    position: absolute; left: 60px; bottom: 84px;
  }
  .holder-name {
    font-weight: 700; font-size: 42px; color: var(--navy);
    text-transform: uppercase; letter-spacing: 0.5px; line-height: 1;
  }
  .holder-role {
    font-weight: 400; font-size: 22px; color: var(--ink); margin-top: 6px;
  }

  .contact {
    position: absolute; right: 56px; bottom: 62px;
    list-style: none;
    font-size: 21px; color: var(--ink);
  }
  .contact-item {
    display: flex; align-items: center; gap: 12px; line-height: 1.5;
    white-space: nowrap;
  }
  .contact-icon { width: 20px; height: 20px; flex: none; }
</style>
</head>
<body>
  <main class="sheet">
    <section class="card card--front" aria-label="Card front">
      <div class="brand">
        <h1 class="brand-name">Brightvale Holdings, LLC</h1>
        <span class="brand-mark" aria-hidden="true"></span>
      </div>
    </section>

    <section class="card card--back" aria-label="Card back">
      <div class="brand">
        <h2 class="brand-name">Brightvale Holdings, LLC</h2>
        <span class="brand-mark" aria-hidden="true"></span>
      </div>

      <div class="holder">
        <p class="holder-name">Milo Jarvis</p>
        <p class="holder-role">Business Development</p>
      </div>

      <ul class="contact">
        <li class="contact-item">
          <svg class="contact-icon" viewBox="0 0 24 24" aria-hidden="true">
            <path fill="#1f3a78" d="M6.6 10.8a15.1 15.1 0 0 0 6.6 6.6l2.2-2.2c.3-.3.7-.4 1-.2 1.1.4 2.3.6 3.6.6.6 0 1 .4 1 1V20c0 .6-.4 1-1 1A17 17 0 0 1 3 4c0-.6.4-1 1-1h3.5c.6 0 1 .4 1 1 0 1.3.2 2.5.6 3.6.1.3 0 .7-.2 1z"/>
          </svg>
          <span>+555-382-9047</span>
        </li>
        <li class="contact-item">
          <svg class="contact-icon" viewBox="0 0 24 24" aria-hidden="true">
            <rect x="2" y="5" width="20" height="14" fill="#1f3a78"/>
            <path d="M2 5l10 8 10-8M2 19l7-7M22 19l-7-7" stroke="#fdfdfd" stroke-width="1.4" fill="none"/>
          </svg>
          <span>sales@brightvaleholdingsllc.example</span>
        </li>
      </ul>
    </section>
  </main>
</body>
</html>
```